Business Card Design for Venture Kite

Venture Kite is a pro bono student consultancy service offered by Corvala KTRB to social start ups and enterprises. We provide consulting services with expertise in areas such as Marketing, IT, Business Strategy and Innovation.
I have attached\ the Venture Kite Logo here for your perusal.
Industry/Entity Type
Business
Contact Information for Business Card
Name: Ha Min Park Name: Thomas Leung
Role: Project Leader Role: Vice Project Leader
M:0477203941 M: 0479352806
E: ha-min.park@corvalaktrb.org E: thomas.leung@corvalaktrb.org
W: www.corvalaktrb.org W: www.corvalaktrb.org

```html
<!DOCTYPE html>
<html lang="en">
<head>
<meta charset="utf-8">
<title>Venture Kite – Business Card</title>
<link rel="stylesheet" href="https://fonts.googleapis.com/css2?family=Arimo:wght@400&display=swap">
<style>
  :root {
    --backdrop: #ece9e4;
    --card-white: #ffffff;
    --brand-orange: #f7931e;
    --ink: #111111;
    --text-dark: #2a2a2a;
    --peach-light: #fbe6d6;
    --peach-mid: #f3c9a8;
    --peach-deep: #e9b492;
  }
  * { box-sizing: border-box; margin: 0; padding: 0; }
  html, body {
    width: 1200px; height: 781px; overflow: hidden;
    background: var(--backdrop);
  }
  .canvas {
    position: relative; width: 1200px; height: 781px;
    display: flex; align-items: center; justify-content: center; gap: 44px;
  }
  .card {
    position: relative; width: 540px; height: 310px; overflow: hidden;
    box-shadow: 0 6px 18px rgba(0,0,0,0.18);
  }
  .band { position: absolute; left: 0; right: 0; background: var(--brand-orange); }

  /* Front */
  .card-front { background: var(--card-white); }
  .card-front .band-top { top: 0; height: 30px; }
  .card-front .band-bottom { bottom: 0; height: 30px; }
  .brand-name {
    font-family: "Arimo", "Arial", sans-serif; font-weight: 400;
    color: var(--ink); line-height: 1; white-space: nowrap;
  }
  .brand-line-1 { position: absolute; left: 40px; top: 62px; font-size: 80px; }
  .brand-line-2 { position: absolute; right: 48px; top: 152px; font-size: 56px; }
  .accent-line { position: absolute; height: 6px; background: var(--brand-orange); }
  .accent-upper { left: 370px; width: 130px; top: 130px; }
  .accent-lower { left: 40px; width: 300px; top: 198px; }

  /* Back */
  .card-back { background: var(--peach-mid); }
  .back-glow {
    position: absolute; inset: 0;
    background:
      radial-gradient(ellipse at 62% 38%, #fff7ee 0%, rgba(255,240,225,0.7) 22%, rgba(243,201,168,0) 60%),
      linear-gradient(135deg, var(--peach-light) 0%, var(--peach-mid) 55%, var(--peach-deep) 100%);
  }
  .card-back .band-top { top: 0; height: 14px; }
  .card-back .band-bottom { bottom: 0; height: 16px; }
  .contacts {
    position: absolute; left: 28px; top: 38px;
    font-family: "Arimo", "Arial", sans-serif; color: var(--text-dark);
  }
  .person + .person { margin-top: 16px; }
  .person-name { font-size: 17px; line-height: 24px; }
  .contact-row { display: flex; align-items: center; gap: 10px; font-size: 16px; line-height: 24px; }
  .contact-icon { width: 20px; height: 20px; flex: none; }
</style>
</head>
<body>
<main class="canvas">
  <section class="card card-front">
    <div class="band band-top"></div>
    <h1 aria-label="Venture Kite">
      <span class="brand-name brand-line-1">Venture</span>
      <span class="brand-name brand-line-2">Kite</span>
    </h1>
    <div class="accent-line accent-upper"></div>
    <div class="accent-line accent-lower"></div>
    <div class="band band-bottom"></div>
  </section>

  <section class="card card-back">
    <div class="back-glow" role="img" aria-label="Soft peach light-burst background"></div>
    <div class="band band-top"></div>
    <div class="contacts">
      <div class="person">
        <p class="person-name">Ha Min Park (Project Leader)</p>
        <p class="contact-row">
          <svg class="contact-icon" viewBox="0 0 20 20"><circle cx="10" cy="10" r="9" fill="none" stroke="#222" stroke-width="1.5"/><rect x="7" y="4.5" width="6" height="11" rx="1" fill="#222"/><rect x="8" y="6" width="4" height="6.5" fill="#fbe6d6"/></svg>
          0477203941
        </p>
        <p class="contact-row">
          <svg class="contact-icon" viewBox="0 0 20 20"><circle cx="10" cy="10" r="9" fill="none" stroke="#222" stroke-width="1.5"/><rect x="5" y="6.5" width="10" height="7" fill="none" stroke="#222" stroke-width="1.4"/><path d="M5 6.5 L10 11 L15 6.5" fill="none" stroke="#222" stroke-width="1.4"/></svg>
          ha-min.park@corvalaktrb.org
        </p>
        <p class="contact-row">
          <svg class="contact-icon" viewBox="0 0 20 20"><circle cx="10" cy="10" r="9" fill="none" stroke="#222" stroke-width="1.5"/><circle cx="10" cy="10" r="5.5" fill="none" stroke="#222" stroke-width="1.2"/><ellipse cx="10" cy="10" rx="2.4" ry="5.5" fill="none" stroke="#222" stroke-width="1"/><path d="M4.5 10 H15.5" stroke="#222" stroke-width="1"/></svg>
          www.corvalaktrb.org
        </p>
      </div>
      <div class="person">
        <p class="person-name">Thomas Leung (Vice Project Leader)</p>
        <p class="contact-row">
          <svg class="contact-icon" viewBox="0 0 20 20"><circle cx="10" cy="10" r="9" fill="none" stroke="#222" stroke-width="1.5"/><rect x="7" y="4.5" width="6" height="11" rx="1" fill="#222"/><rect x="8" y="6" width="4" height="6.5" fill="#fbe6d6"/></svg>
          0479352806
        </p>
        <p class="contact-row">
          <svg class="contact-icon" viewBox="0 0 20 20"><circle cx="10" cy="10" r="9" fill="none" stroke="#222" stroke-width="1.5"/><rect x="5" y="6.5" width="10" height="7" fill="none" stroke="#222" stroke-width="1.4"/><path d="M5 6.5 L10 11 L15 6.5" fill="none" stroke="#222" stroke-width="1.4"/></svg>
          thomas.leung@corvalaktrb.org
        </p>
        <p class="contact-row">
          <svg class="contact-icon" viewBox="0 0 20 20"><circle cx="10" cy="10" r="9" fill="none" stroke="#222" stroke-width="1.5"/><circle cx="10" cy="10" r="5.5" fill="none" stroke="#222" stroke-width="1.2"/><ellipse cx="10" cy="10" rx="2.4" ry="5.5" fill="none" stroke="#222" stroke-width="1"/><path d="M4.5 10 H15.5" stroke="#222" stroke-width="1"/></svg>
          www.corvalaktrb.org
        </p>
      </div>
    </div>
    <div class="band band-bottom"></div>
  </section>
</main>
</body>
</html>
```